IT Tradingsystem for car dealers needs Business Card Design

We need a fresh and modern design for our new business cards.

We develop a it-business system for car dealers in Sweden, Norway and on our way down to further countries in Europe, hence the namechange to BrolaTek Europe AB. The site can be found at www.brolatek-example.com. The startpage is also in for an update/modernization soon so don't take to much from here.

We are looking to print double sided, 4-colour cards.

We want to look professional, modern and serious. Open to cooler suggestions, but not too crazy. We need to make a good and serious impression on our potential customers. It needs to reflect our scandinavian design values and layout.

Preferably with the full BrolaTek logo in good size on the back, so the small print on the logo can be read easily.

Text that needs to go on the cards:
-------

Per Oskar Fjellström
Founder

Direct +46 70-512 96 47
Support 08-612 57 394
po.fjellstrom@brolatek-example.com

BrolaTek Europe AB
Box 8617
104 29 Stockholm

Brolatek-example.com
Saljportalen-example.se

--------
Good luck and thanks!

PS. If you need more input or see what our previous cards looked like, don't hesitate to contact me!

Target Market(s)

Decision makers / executives at brand cardealers

Industry/Entity Type

Automotive

Contact Information for Business Card

Normal size

Requirements
Must have
• Full logo
Nice to have
• Base on our orange colors
Should not have
• No fonts with serif, and not too much graphics

```html
<!DOCTYPE html>
<html lang="sv">
<head>
<meta charset="utf-8">
<title>BrolaTek – Business Card</title>
<link rel="stylesheet" href="https://fonts.googleapis.com/css2?family=Quicksand:wght@400;500;700&display=swap">
<style>
  :root {
    --orange: #f47f20;
    --orange-light: #f9a35a;
    --black: #0d0d0d;
    --black-soft: #1c1c1c;
    --white: #f4f4f4;
    --grey-text: #5e5e5e;
    --grey-mid: #7a7a7a;
    --stage: #3a2d22;
  }
  * { box-sizing: border-box; margin: 0; padding: 0; }
  html, body {
    width: 1200px; height: 900px; overflow: hidden;
    background: var(--stage);
    font-family: "Quicksand", sans-serif;
  }
  .canvas { position: relative; width: 1200px; height: 900px; }

  .card {
    position: absolute; left: 260px;
    width: 680px; height: 400px;
    overflow: hidden;
    box-shadow: 0 10px 30px rgba(0,0,0,.45);
  }

  /* Front */
  .card--front {
    top: 35px;
    background: radial-gradient(ellipse at 35% 45%, #2a2a2a 0%, var(--black) 70%);
  }
  .front__faint-art {
    position: absolute; left: 140px; top: 215px; width: 300px; height: 120px;
    border-radius: 60px 80px 20px 20px;
    background: radial-gradient(ellipse, rgba(255,255,255,.035), rgba(255,255,255,0) 70%);
  }
  .brand { display: flex; align-items: center; gap: 14px; }
  .brand__mark { width: 34px; height: 34px; background: var(--orange); }
  .brand__name { font-weight: 700; font-size: 46px; color: #fff; letter-spacing: .5px; line-height: 1; }
  .front__brand { position: absolute; left: 90px; top: 150px; }
  .tagline { font-weight: 500; font-size: 12.5px; color: #ddd; letter-spacing: .5px; }
  .front__tagline { position: absolute; left: 138px; top: 204px; }
  .front__web {
    position: absolute; right: 36px; bottom: 26px;
    display: flex; gap: 28px;
    color: var(--orange); font-size: 16px; font-weight: 500; letter-spacing: .5px;
  }

  /* Back */
  .card--back { top: 465px; background: var(--white); }
  .back__dark {
    position: absolute; left: 0; top: 0; width: 385px; height: 100%;
    background: radial-gradient(ellipse at 40% 40%, #262626 0%, var(--black) 75%);
  }
  .back__brand { position: absolute; left: 70px; top: 125px; }
  .back__brand .brand__mark { width: 48px; height: 48px; }
  .back__brand .brand__name { color: var(--orange); font-size: 56px; }

  .address-band {
    position: absolute; left: 0; top: 285px; width: 385px; height: 70px;
    background: var(--orange);
    display: flex; align-items: center; gap: 14px; padding-left: 24px;
  }
  .address-band__pin {
    width: 30px; height: 30px; border-radius: 50%;
    border: 2px solid rgba(255,255,255,.75);
    display: flex; align-items: center; justify-content: center;
  }
  .address-band__text { color: #fde3cb; font-size: 17px; font-weight: 500; line-height: 1.2; letter-spacing: .3px; }

  .name-banner {
    position: absolute; left: 300px; top: 38px; width: 380px; height: 36px;
    background: var(--orange);
    display: flex; align-items: center; padding-left: 74px;
    color: #fff; font-weight: 700; font-size: 17px; letter-spacing: 1px; text-transform: uppercase;
  }
  .role { position: absolute; left: 458px; top: 86px; font-size: 18px; color: var(--grey-text); font-weight: 500; }

  .contacts { position: absolute; left: 400px; top: 128px; list-style: none; }
  .contacts__item {
    display: flex; align-items: center; gap: 12px; height: 38px;
    font-size: 15px; color: #333; font-weight: 500; letter-spacing: .2px;
  }
  .contacts__icon {
    width: 26px; height: 26px; border-radius: 50%; background: var(--orange);
    display: flex; align-items: center; justify-content: center; flex: none;
  }
  .contacts__email { font-size: 13px; }

  .back__wordmark {
    position: absolute; left: 398px; top: 262px;
    font-weight: 700; font-size: 56px; color: var(--grey-mid); line-height: 1;
  }
  .back__tagline { position: absolute; left: 430px; top: 326px; color: var(--grey-mid); font-size: 13px; }
</style>
</head>
<body>
<main class="canvas">

  <section class="card card--front" aria-label="Card front">
    <div class="front__faint-art" role="img" aria-label="Faint outline of a car"></div>
    <div class="brand front__brand">
      <span class="brand__mark"></span>
      <span class="brand__name">BrolaTek</span>
    </div>
    <p class="tagline front__tagline">Bilkoll | Remarketing | saljportalen-example.se</p>
    <p class="front__web"><span>Brolatek-example.com</span><span>Saljportalen-example.se</span></p>
  </section>

  <section class="card card--back" aria-label="Card back">
    <div class="back__dark"></div>
    <div class="brand back__brand">
      <span class="brand__mark"></span>
      <span class="brand__name">BrolaTek</span>
    </div>

    <div class="address-band">
      <span class="address-band__pin">
        <svg width="14" height="16" viewBox="0 0 14 16"><path d="M7 0a6 6 0 0 0-6 6c0 4.5 6 10 6 10s6-5.5 6-10a6 6 0 0 0-6-6zm0 8.5A2.5 2.5 0 1 1 7 3.5a2.5 2.5 0 0 1 0 5z" fill="#fde3cb"/></svg>
      </span>
      <p class="address-band__text">BrolaTek Europe AB<br>Box 8617, 104 29 Stockholm</p>
    </div>

    <h1 class="name-banner">Per Oskar Fjellström</h1>
    <p class="role">Founder</p>

    <ul class="contacts">
      <li class="contacts__item">
        <span class="contacts__icon"><svg width="10" height="15" viewBox="0 0 10 15"><rect x="1" y="1" width="8" height="13" rx="1.5" fill="none" stroke="#fff" stroke-width="1.5"/><rect x="3" y="3" width="4" height="5" fill="#fff"/></svg></span>
        +46 70-512 96 47
      </li>
      <li class="contacts__item">
        <span class="contacts__icon"><svg width="14" height="14" viewBox="0 0 14 14"><path d="M3 1l2.5 3-1.5 1.5c.8 1.8 2.2 3.2 4 4L9.5 8 12.5 10.5 11 13C6 13 1 8 1 3z" fill="#fff"/></svg></span>
        08-612 57 394
      </li>
      <li class="contacts__item">
        <span class="contacts__icon"><svg width="14" height="10" viewBox="0 0 14 10"><rect x=".75" y=".75" width="12.5" height="8.5" fill="none" stroke="#fff" stroke-width="1.5"/><path d="M1 1l6 5 6-5" fill="none" stroke="#fff" stroke-width="1.5"/></svg></span>
        <span class="contacts__email">po.fjellstrom@brolatek-example.com</span>
      </li>
    </ul>

    <p class="back__wordmark">BrolaTek</p>
    <p class="tagline back__tagline">Bilkoll | Remarketing | saljportalen-example.se</p>
  </section>

</main>
</body>
</html>
```